Anzeigengestaltung für Workshops
Zielgruppe
Die KTW-Academy realisiert Workshops für Medienschaffende. Im konkreten Fall soll ein 1-tägiger Workshop für Sprecher*innen in Radio, Podcast und Voice-Over beworben werden.
Aufgabenstellung
Die Anzeige soll in den verschiedenen Social-Media-Kanälen ausgespielt werden. Sie soll cool sein, eher minimalistisch, keinesfalls verspielt oder knallig.
Textbausteine sind:
Die Kunst des ruhigen Atems bei Tag [das ist der Titel der Veranstaltung]
Wie Du gut rüberkommst als Sprecher*in in Radio, Podcast und Voice-Over [das ist die Unterzeile]
Präsenz-Training | KTW-Funkhaus | 15.9.2023 [das sind die Rahmendaten]
ggfs. mit Störer 'jetzt buchen' o.ä.
Logo und Bild der Trainerin sind verpflichtend

```html
<!DOCTYPE html>
<html lang="de">
<head>
<meta charset="utf-8">
<title>KTW-Academy – Die Kunst des ruhigen Atems bei Tag</title>
<link rel="stylesheet" href="https://fonts.googleapis.com/css2?family=Anton&family=Barlow+Condensed:wght@400;700&display=swap">
<style>
  :root {
    --green: #9ac321;
    --white: #ffffff;
    --black: #000000;
    --red: #c30f12;
    --photo-light: #c9c3b4;
    --photo-dark: #3a3a36;
  }
  * { margin: 0; padding: 0; box-sizing: border-box; }
  html, body { width: 1200px; height: 1200px; overflow: hidden; background: var(--green); }
  .ad {
    position: relative;
    width: 1200px;
    height: 1200px;
    background: var(--green);
    overflow: hidden;
  }
  .ad__band {
    position: absolute;
    left: 0;
    top: 105px;
    width: 100%;
    height: 436px;
    background: var(--white);
  }
  .ad__title {
    position: absolute;
    left: 78px;
    top: 52px;
    font-family: "Anton", "Impact", sans-serif;
    font-weight: 400;
    font-size: 146px;
    line-height: 157px;
    color: var(--black);
    text-shadow: -7px -7px 0 var(--white);
    letter-spacing: 1px;
  }
  .ad__subline {
    position: absolute;
    right: 461px;
    top: 560px;
    font-family: "Barlow Condensed", "Arial Narrow", sans-serif;
    font-weight: 400;
    font-size: 50px;
    line-height: 68px;
    text-align: right;
    color: var(--black);
  }
  .ad__trainer-photo {
    position: absolute;
    left: 806px;
    top: 413px;
    width: 334px;
    height: 363px;
    border-radius: 16px 16px 0 0;
    background: linear-gradient(180deg, var(--photo-light) 0%, #b59a78 45%, var(--photo-dark) 100%);
  }
  .ad__academy-name {
    position: absolute;
    left: 806px;
    top: 790px;
    width: 334px;
    display: flex;
    align-items: center;
    gap: 14px;
    font-family: "Anton", "Impact", sans-serif;
    font-size: 48px;
    line-height: 1;
    color: var(--black);
  }
  .ad__academy-name::before {
    content: "";
    width: 26px;
    height: 26px;
    background: var(--black);
    flex: none;
  }
  .ad__visual {
    position: absolute;
    left: 75px;
    top: 755px;
    width: 460px;
    height: 413px;
    border-radius: 230px 230px 24px 24px;
    background: linear-gradient(180deg, #2c3a10 0%, #111 100%);
  }
  .ad__stoerer {
    position: absolute;
    left: 466px;
    top: 761px;
    width: 254px;
    height: 254px;
    border-radius: 50%;
    background: var(--red);
    display: flex;
    align-items: center;
    justify-content: center;
  }
  .ad__stoerer-text {
    font-family: "Anton", "Impact", sans-serif;
    font-size: 46px;
    line-height: 54px;
    color: var(--white);
    text-align: center;
    transform: rotate(-16deg);
  }
  .ad__details {
    position: absolute;
    left: 806px;
    top: 960px;
    width: 340px;
    font-family: "Barlow Condensed", "Arial Narrow", sans-serif;
    font-weight: 700;
    font-size: 52px;
    line-height: 68px;
    text-align: center;
    color: var(--black);
  }
</style>
</head>
<body>
  <main class="ad">
    <div class="ad__band"></div>

    <h1 class="ad__title">Die Kunst des<br>ruhigen Atems<br>bei Tag</h1>

    <p class="ad__subline">Wie Du gut rüberkommst als<br>Sprecher*in in Radio, Podcast<br>und Voice-Over</p>

    <div class="ad__trainer-photo" role="img" aria-label="Porträtfoto der Trainerin"></div>

    <div class="ad__academy-name">KTW-Academy</div>

    <div class="ad__visual" role="img" aria-label="Illustration: Kopfhörer mit Herz und Schallwellen"></div>

    <div class="ad__stoerer">
      <p class="ad__stoerer-text">JETZT<br>BUCHEN!</p>
    </div>

    <p class="ad__details">Präsenz-Training<br>KTW-Funkhaus<br>15.9.2023</p>
  </main>
</body>
</html>
```